Design a Future- POV MOTSAVIN

Refresh the images/Theme. Focus theme/images on the following

1. Adaptability
2. Resilience
3. Emotional Inteligence
4. Relentless execution
5. High Care Factor

Industry/Entity Type

Technology Equipment

Font styles to use
Other font styles liked:
• Cisco Sans

Colors
33a6d7
cfdeed
85acd3
85cae6
fcf7c1
3377b5
fee18a

Requirements
Must have
• Consistent theme
Professional almost marketing look and feel
Nice to have
• none
Should not have
• none

```html
<!DOCTYPE html>
<html lang="en">
<head>
<meta charset="utf-8">
<title>Future Point of View – Motsavin</title>
<link href="https://fonts.googleapis.com/css2?family=Open+Sans:wght@400;600;700;800&display=swap" rel="stylesheet">
<style>
  :root{
    --blue:#3377b5;
    --sky:#33a6d7;
    --ice:#cfdeed;
    --steel:#85acd3;
    --aqua:#85cae6;
    --cream:#fcf7c1;
    --gold:#fee18a;
    --navy:#1d3f66;
    --ink:#2b3440;
    --mute:#7c8896;
    --page:#ffffff;
  }
  *{box-sizing:border-box;margin:0;padding:0}
  html,body{width:773px;height:1200px;overflow:hidden;background:var(--page)}
  body{position:relative;font-family:"Open Sans",Arial,sans-serif;color:var(--ink)}
  .slide{position:absolute;width:318px;height:208px;overflow:hidden;background:#fff;box-shadow:0 1px 4px rgba(0,0,0,.18)}
  .col-a{left:36px}.col-b{left:420px}
  .row-1{top:27px}.row-2{top:261px}.row-3{top:488px}.row-4{top:715px}.row-5{top:940px}
  .photo{position:absolute}
  .abs{position:absolute}
  .tiny{font-size:4.6px;line-height:1.45}
  .pagenum{position:absolute;right:6px;bottom:4px;font-size:4px;color:var(--mute)}

  /* title */
  .title-slide{background:linear-gradient(120deg,#1b4f86 0%,var(--blue) 45%,var(--sky) 100%)}
  .title-slide .photo{right:0;top:0;width:150px;height:208px;background:linear-gradient(160deg,rgba(207,222,237,.45),rgba(51,119,181,0))}
  .title-slide .headline{position:absolute;left:22px;top:70px;display:flex;align-items:center;gap:8px}
  .title-slide h1{font-size:20px;font-weight:800;color:#fff;white-space:nowrap}
  .title-slide .sub{font-size:7px;color:var(--ice);line-height:1.1;font-weight:600;white-space:nowrap}
  .title-slide .meta{position:absolute;left:22px;top:100px;color:var(--ice)}

  /* agenda */
  .agenda .photo{left:0;top:0;width:150px;height:208px;background:linear-gradient(135deg,#f1f3f5,#cfd6dd 60%,#b9c3cc)}
  .agenda h2{position:absolute;left:32px;top:20px;font-size:17px;font-weight:700;color:var(--blue)}
  .agenda ol{position:absolute;left:205px;top:28px;list-style:none}
  .agenda li{font-size:5px;color:var(--ink);margin-bottom:9px;display:flex;gap:6px}
  .agenda li b{color:var(--sky)}

  /* what matters */
  .matters h2{position:absolute;left:16px;top:14px;font-size:14px;font-weight:800;color:var(--navy)}
  .matters .lead{position:absolute;left:16px;top:34px;width:200px;color:var(--mute)}
  .collage{position:absolute;left:16px;top:62px;width:286px;height:130px;display:grid;grid-template-columns:repeat(5,1fr);gap:3px}
  .collage div{background:linear-gradient(160deg,var(--steel),#5b6f85)}
  .collage div:nth-child(2n){background:linear-gradient(160deg,var(--ice),#8b97a6)}
  .collage div:nth-child(3n){background:linear-gradient(160deg,#c9a86a,#5f5240)}

  /* philosophy */
  .philosophy .photo{left:0;top:0;width:170px;height:208px;background:linear-gradient(135deg,#f6d77a,#d4a33b 55%,#7a5b24)}
  .philosophy h2{position:absolute;left:106px;top:12px;font-size:9.5px;font-weight:700;color:#fff;width:66px;line-height:1.15}
  .philosophy .formula{position:absolute;left:106px;top:48px;width:64px;height:110px;background:var(--blue);color:#fff;padding:8px 7px;font-size:8px;font-weight:700;line-height:1.2}
  .philosophy .caps{position:absolute;left:182px;top:16px;width:126px;height:178px;background:#f1f4f8;padding:10px}
  .caps h3{font-size:9px;font-weight:700;color:var(--navy);margin-bottom:10px}
  .caps span{display:block;background:var(--sky);color:#fff;font-size:5.5px;font-weight:600;text-align:center;padding:6px 0;margin-bottom:7px}

  /* why me */
  .whyme{background:var(--blue)}
  .whyme .photo{right:0;top:0;width:318px;height:208px;background:linear-gradient(100deg,rgba(51,119,181,0) 40%,rgba(29,63,102,.8))}
  .whyme h2{position:absolute;left:16px;top:16px;font-size:15px;font-weight:800;color:#fff;line-height:1.05}
  .whyme h2 em{font-style:normal;color:var(--gold)}
  .whyme .lead{position:absolute;left:16px;top:56px;font-size:6.5px;color:#fff;font-weight:600;width:130px}
  .whyme ul{position:absolute;left:16px;top:84px;width:120px;color:var(--ice);list-style:none}
  .whyme .panels{position:absolute;left:152px;top:38px;width:100px}
  .whyme .panels div{background:var(--navy);color:#fff;padding:5px;margin-bottom:4px}
  .whyme .panels b{display:block;font-size:5px;color:var(--gold)}

  /* 30-60-90 */
  .plan{background:linear-gradient(135deg,#2c3a48,#55616c 50%,#2a2f36)}
  .plan h2{position:absolute;left:120px;top:14px;font-size:13px;font-weight:700;color:#fff}
  .plan .cards{position:absolute;left:60px;top:44px;display:flex;gap:8px}
  .plan .card{width:70px;height:140px;background:#fff}
  .plan .card h3{background:var(--blue);color:#fff;font-size:6.5px;text-align:center;padding:5px 0}
  .plan .card p{padding:5px;color:var(--ink)}

  /* goals */
  .goals .photo{left:0;top:0;width:118px;height:208px;background:linear-gradient(180deg,#d7e4d2,#8fb06a 55%,#5a4630)}
  .goals h2{position:absolute;left:14px;top:30px;background:var(--sky);color:#fff;font-size:12px;font-weight:800;padding:5px 10px;line-height:1.05}
  .goals ul,.success ul{position:absolute;list-style:none}
  .goals ul{left:140px;top:22px}
  .row{display:flex;align-items:center;gap:7px;margin-bottom:8px;font-size:5px;color:var(--ink)}
  .row i{width:14px;height:14px;background:var(--blue);display:flex;align-items:center;justify-content:center}

  /* fy success */
  .success .photo{left:0;top:0;width:150px;height:208px;background:linear-gradient(150deg,#a9c7e3,var(--blue) 50%,#1d3f66)}
  .success h2{position:absolute;left:14px;top:46px;font-size:12px;font-weight:700;color:#fff;line-height:1.1}
  .success ul{left:176px;top:30px}

  /* sponsors */
  .sponsors h2{position:absolute;left:16px;top:14px;font-size:15px;font-weight:800;color:var(--navy)}
  .people{position:absolute;left:16px;top:72px;display:flex;gap:8px}
  .person{width:50px;text-align:center}
  .person .photo{position:static;width:50px;height:58px;background:linear-gradient(180deg,#dfe6ee,#9aa9ba)}
  .person span{display:block;background:var(--gold);font-size:4.4px;padding:2px 0;margin-top:3px;color:var(--ink)}

  /* thank you */
  .thanks .photo{left:0;top:0;width:318px;height:208px;background:linear-gradient(180deg,var(--sky) 0%,var(--aqua) 40%,#e9f2f8 70%,#b8cde0)}
  .thanks h2{position:absolute;right:24px;top:14px;font-size:16px;font-weight:800;color:#fff}
  .thanks .meta{position:absolute;right:24px;top:36px;color:#fff;font-weight:600}
</style>
</head>
<body>

<section class="slide col-a row-1 title-slide">
  <div class="photo" role="img" aria-label="Blue-toned modern office building"></div>
  <div class="headline">
    <h1>New Role</h1>
    <div class="sub">Point of View<br>Document</div>
  </div>
  <div class="meta tiny">B. Motsavin<br>June 2024</div>
</section>

<section class="slide col-b row-1 agenda">
  <div class="photo" role="img" aria-label="Notebook and pen on a desk"></div>
  <h2>Agenda</h2>
  <ol>
    <li><b>01</b>Overview</li>
    <li><b>02</b>Leadership Philosophy</li>
    <li><b>03</b>Qualifications</li>
    <li><b>04</b>30-60-90 Day Plan</li>
    <li><b>05</b>90 Day Goals</li>
    <li><b>06</b>FY Define Success</li>
    <li><b>07</b>Sponsors</li>
    <li><b>08</b>Appendix</li>
  </ol>
</section>

<section class="slide col-a row-2 matters">
  <h2>My “What Matters?”</h2>
  <p class="lead tiny">Servant Leadership – “Why We Care” – Mission Driven to Impact – Guided by Purpose and Team</p>
  <div class="collage" role="img" aria-label="Collage of team and family photos">
    <div></div><div></div><div></div><div></div><div></div>
    <div></div><div></div><div></div><div></div><div></div>
  </div>
  <span class="pagenum">3</span>
</section>

<section class="slide col-b row-2 philosophy">
  <div class="photo" role="img" aria-label="Golden light over a city skyline"></div>
  <h2>Leadership<br>Philosophy</h2>
  <div class="formula">My formula for success has been</div>
  <div class="caps">
    <h3>Key Capabilities</h3>
    <span>Servant Leading</span><span>Modeling</span><span>Executing</span><span>Coaching</span>
  </div>
</section>

<section class="slide col-a row-3 whyme">
  <div class="photo" role="img" aria-label="Blue tinted team at work"></div>
  <h2>Why <em>Me</em><br>&amp; Why <em>This Role</em></h2>
  <p class="lead">Execute for Results; Care for Culture</p>
  <ul class="tiny">
    <li>• Proven growth in every market</li>
    <li>• Leadership across regions</li>
    <li>• Strong partner alignment</li>
    <li>• Deep customer relationships</li>
    <li>• Trusted by peers and teams</li>
  </ul>
  <div class="panels tiny">
    <div><b>Results</b>Exceeded plan four years running</div>
    <div><b>Culture</b>Built high trust, high care teams</div>
    <div><b>Why Now</b>Ready to scale impact further</div>
  </div>
</section>

<section class="slide col-b row-3 plan">
  <div class="abs" role="img" aria-label="Dark desk with laptop" style="inset:0"></div>
  <h2>30-60-90 Day Plan</h2>
  <div class="cards">
    <div class="card"><h3>People</h3><p class="tiny">Meet every team member. Listen first, learn roles, build trust.</p></div>
    <div class="card"><h3>Pipeline</h3><p class="tiny">Review open deals, align forecasts, find quick wins.</p></div>
    <div class="card"><h3>Process</h3><p class="tiny">Simplify cadence, set metrics, drive clear execution.</p></div>
  </div>
</section>

<section class="slide col-a row-4 goals">
  <div class="photo" role="img" aria-label="Young plant sprouting from soil"></div>
  <h2>90 day<br>Goals</h2>
  <ul>
    <li class="row"><i><svg width="8" height="8" viewBox="0 0 8 8"><path d="M1 4l2 2 4-4" stroke="#fff" fill="none"/></svg></i>Foundation in our culture</li>
    <li class="row"><i><svg width="8" height="8" viewBox="0 0 8 8"><path d="M1 4l2 2 4-4" stroke="#fff" fill="none"/></svg></i>Establish team cadence</li>
    <li class="row"><i><svg width="8" height="8" viewBox="0 0 8 8"><path d="M1 4l2 2 4-4" stroke="#fff" fill="none"/></svg></i>All hires in place by Q2</li>
    <li class="row"><i><svg width="8" height="8" viewBox="0 0 8 8"><path d="M1 4l2 2 4-4" stroke="#fff" fill="none"/></svg></i>Quarterly alignment on plan</li>
    <li class="row"><i><svg width="8" height="8" viewBox="0 0 8 8"><path d="M1 4l2 2 4-4" stroke="#fff" fill="none"/></svg></i>Build customer trust</li>
    <li class="row"><i><svg width="8" height="8" viewBox="0 0 8 8"><path d="M1 4l2 2 4-4" stroke="#fff" fill="none"/></svg></i>Review pipeline</li>
  </ul>
</section>

<section class="slide col-b row-4 success">
  <div class="photo" role="img" aria-label="Blue glass building facade"></div>
  <h2>FY –<br>Define Success</h2>
  <ul>
    <li class="row"><i><svg width="8" height="8" viewBox="0 0 8 8"><path d="M1 6l2-2 2 1 2-4" stroke="#fff" fill="none"/></svg></i>Grow team bookings</li>
    <li class="row"><i><svg width="8" height="8" viewBox="0 0 8 8"><path d="M1 6l2-2 2 1 2-4" stroke="#fff" fill="none"/></svg></i>Retain top talent</li>
    <li class="row"><i><svg width="8" height="8" viewBox="0 0 8 8"><path d="M1 6l2-2 2 1 2-4" stroke="#fff" fill="none"/></svg></i>Customer success ahead of plan</li>
    <li class="row"><i><svg width="8" height="8" viewBox="0 0 8 8"><path d="M1 6l2-2 2 1 2-4" stroke="#fff" fill="none"/></svg></i>Partner programs scaled</li>
    <li class="row"><i><svg width="8" height="8" viewBox="0 0 8 8"><path d="M1 6l2-2 2 1 2-4" stroke="#fff" fill="none"/></svg></i>Engaged, caring culture</li>
  </ul>
</section>

<section class="slide col-a row-5 sponsors">
  <h2>Sponsors</h2>
  <div class="people">
    <div class="person"><div class="photo" role="img" aria-label="Sponsor portrait"></div><span>A. Lindqvist</span></div>
    <div class="person"><div class="photo" role="img" aria-label="Sponsor portrait"></div><span>R. Okafor</span></div>
    <div class="person"><div class="photo" role="img" aria-label="Sponsor portrait"></div><span>J. Tremont</span></div>
    <div class="person"><div class="photo" role="img" aria-label="Sponsor portrait"></div><span>M. Haldane</span></div>
    <div class="person"><div class="photo" role="img" aria-label="Sponsor portrait"></div><span>P. Verhoek</span></div>
  </div>
  <span class="pagenum">9</span>
</section>

<section class="slide col-b row-5 thanks">
  <div class="photo" role="img" aria-label="Snowy mountain peak under blue sky"></div>
  <h2>Thank you!</h2>
  <div class="meta tiny">B. Motsavin</div>
</section>

</body>
</html>
```